8-page Visitor's Guide for Private Wildlife Ranch

We need a Visitor's Guide for Private Wildlife Ranch, where we can include important information for the clients during their stay as well as the many activities we and surrounding businesses have to offer... we are looking to keep it in line with our current web look and feel, as well as some of the included supporting documents, our rack card and our current tribe-fold brochure... I will be looking to update these as well in the near future with a supporting design... just looking for something a little more eye catching and up to date!

http:// mbxq.example.org/leaflets/qrsleaf/files/mbx_lf_q7111_2222zz.

the pdf above is something we really like!!!!

Im sure you are going to need more photos, but I was limited to what I could upload!

www. klcreeksidelodge. com is our website

Info about us: Are you looking for a truly unique Texas experience? K.L. Creekside Lodge is THE place! Whether you are looking for a day trip, a weekend adventure, or a place to host your next event or corporate retreat, join us at K.L. Creekside Lodge.

No matter what your needs and interests are, we offer a wide variety of activities to suit any group. K.L. Creekside Lodge has been the chosen destination for many weddings, events, and corporate retreats.

Target Market(s)

Tourism/Travel

Industry/Entity Type

Tourism

Font styles to use
Other font styles liked:
• Plantagenet Cherokee

Colors
fff3d1
ffffff

Requirements
Must have
• I have included a pdf with a lot of the text that I want.....
• Pages to include: Cover page, Important Information, Welcome Letter/Map, What to do while here, special events at the ranch, lodging options, things you might see during your stay, and a page for ads from local businesses
• colors
• 3e2a05 dark brown
• d2c0a4 light brown
• f3f2f1 light light brown
• font:
• Plantagenet Cherokee
Nice to have
• I want it to have an easy to read, rustic ranch look like with the feel of our website, but fun and exciting to make it inviting and welcoming
Should not have
• ehh pretty open to most anything but bright colors

```html
<!DOCTYPE html>
<html lang="en">
<head>
<meta charset="utf-8">
<title>K.L. Creekside Lodge – Visitor's Guide Spreads</title>
<link rel="stylesheet" href="https://fonts.googleapis.com/css2?family=Jost:wght@500;700&family=Crimson+Pro:wght@400;500&display=swap">
<style>
  :root {
    --backdrop: #fff3d1;
    --paper: #ffffff;
    --brown-dark: #3e2a05;
    --brown-light: #d2c0a4;
    --brown-faint: #f3f2f1;
    --ring-grey: #c9c6c2;
    --shadow: rgba(60, 40, 10, 0.28);
  }
  * { margin: 0; padding: 0; box-sizing: border-box; }
  html, body { width: 1200px; height: 900px; overflow: hidden; }
  body {
    background: var(--backdrop);
    font-family: "Crimson Pro", Georgia, serif;
    color: var(--brown-dark);
    position: relative;
  }
  .page {
    position: absolute;
    top: 42px;
    width: 506px;
    height: 788px;
    background: var(--paper);
    overflow: hidden;
    box-shadow: 6px 6px 8px var(--shadow);
  }
  .page--meals { left: 85px; }
  .page--events { left: 614px; }

  .faint-name {
    position: absolute;
    font-family: "Jost", sans-serif;
    font-weight: 700;
    color: var(--brown-faint);
    font-size: 46px;
    line-height: 1;
    white-space: nowrap;
  }

  .band { position: absolute; background: var(--brown-light); }
  .headline {
    position: absolute;
    font-family: "Jost", sans-serif;
    font-weight: 700;
    line-height: 1;
  }
  .page-title { font-size: 46px; top: 50px; }
  .sub-title { font-size: 20px; }

  .intro {
    position: absolute;
    top: 112px; left: 0; width: 100%;
    text-align: center;
    font-size: 18px;
  }

  .meal-disc {
    position: absolute;
    left: 70px;
    width: 90px; height: 90px;
    border-radius: 50%;
    background: var(--brown-light);
    display: flex; align-items: center; justify-content: center;
  }
  .meal-time {
    position: absolute;
    left: 186px;
    font-size: 16.5px;
  }

  .photo { position: absolute; }
  .photo--pool {
    left: 362px; top: 163px;
    width: 244px; height: 244px;
    border-radius: 50%;
    border: 6px solid #e6e3df;
    background: radial-gradient(circle at 45% 30%, #b9bcbd 0%, #8b8f86 38%, #4fa3b8 62%, #2f8fa6 80%, #9d9384 100%);
  }
  .photo--giraffe {
    left: 0; top: 576px; width: 506px; height: 212px;
    background: linear-gradient(100deg, #8a5a32 0%, #b98552 30%, #3d5a2c 55%, #6f8f4a 75%, #c9d3d6 100%);
  }
  .photo--deer {
    left: 428px; top: 113px; width: 90px; height: 398px;
    border-radius: 8px;
    border: 5px solid var(--ring-grey);
    background: linear-gradient(180deg, #6d7a4a 0%, #8d7b5e 40%, #6e5a40 70%, #55603a 100%);
  }
  .photo--wedding {
    left: 0; top: 584px; width: 506px; height: 204px;
    background: linear-gradient(180deg, #9fb0a6 0%, #6f8a52 35%, #4f6b35 60%, #7c7760 85%, #6b5d48 100%);
  }
  .chevron { position: absolute; left: 0; width: 506px; }

  .note-line {
    position: absolute;
    top: 443px; left: 0; width: 100%;
    text-align: center;
    font-size: 12.5px;
    word-spacing: 1px;
  }

  .amenities {
    position: absolute;
    top: 512px; left: 69px;
    display: flex;
    z-index: 2;
  }
  .amenity {
    width: 74px;
    text-align: center;
    font-size: 14px;
    line-height: 1.15;
  }
  .amenity svg { display: block; margin: 0 auto 5px; }

  .event { position: absolute; left: 70px; width: 334px; }
  .event-tick { position: absolute; left: -70px; top: 8px; width: 61px; height: 6px; background: var(--brown-light); }
  .event h3 { font-weight: 500; font-size: 16.5px; line-height: 1.2; margin-bottom: 2px; }
  .event p { font-size: 14px; line-height: 15.6px; text-align: justify; font-weight: 500; }

  .quote {
    position: absolute;
    top: 522px; left: 0; width: 506px;
    text-align: center;
    font-size: 26px;
  }
</style>
</head>
<body>

<section class="page page--meals">
  <div class="faint-name" style="top:300px;left:120px;">K.L. Creekside Lodge</div>

  <div class="band" style="left:0;top:68px;width:48px;height:18px;"></div>
  <h1 class="headline page-title" style="left:65px;">Meals</h1>
  <div class="band" style="left:208px;top:68px;width:298px;height:18px;"></div>

  <p class="intro">Typically served buffet style in our chuckwagon</p>

  <div class="photo photo--pool" role="img" aria-label="Photo of the lodge swimming pool with a thatched pavilion"></div>

  <div class="band" style="left:0;top:176px;width:110px;height:28px;"></div>
  <div class="meal-disc" style="top:145px;">
    <svg width="60" height="52" viewBox="0 0 60 52">
      <path d="M14 8c-8 4-11 14-8 24s11 16 18 16c-6-4-9-10-9-18s3-15 9-20c-3-2-6-3-10-2z" fill="var(--brown-dark)"/>
      <path d="M9 16l6 3M6 26l8 1M8 36l7-3M14 44l5-5" stroke="var(--brown-light)" stroke-width="2" fill="none"/>
      <path d="M26 26h22v9a11 11 0 0 1-22 0z" fill="var(--brown-dark)"/>
      <path d="M48 28h3a4 4 0 0 1 0 8h-3v-3h3a1 1 0 0 0 0-2h-3z" fill="var(--brown-dark)"/>
      <path d="M34 22c-3-4 3-6 0-10M41 22c-3-4 3-7 0-12" stroke="var(--brown-dark)" stroke-width="2.2" fill="none"/>
    </svg>
  </div>
  <p class="meal-time" style="top:179px;">Breakfast is served at 8:00 AM</p>

  <div class="band" style="left:0;top:274px;width:110px;height:28px;"></div>
  <div class="meal-disc" style="top:243px;">
    <svg width="56" height="58" viewBox="0 0 56 58" fill="none" stroke="var(--brown-dark)" stroke-width="3" stroke-linecap="round">
      <path d="M28 4v6M14 10l4 5M42 10l-4 5M6 22h6M44 22h6"/>
      <path d="M18 26c6-8 14-8 20 0"/>
      <path d="M22 24v8M26 24v8M24 32v22"/>
      <path d="M33 24c4 3 4 10 0 14v16"/>
    </svg>
  </div>
  <p class="meal-time" style="top:277px;">Lunch is served at Noon</p>

  <div class="band" style="left:0;top:374px;width:110px;height:28px;"></div>
  <div class="meal-disc" style="top:343px;">
    <svg width="62" height="40" viewBox="0 0 62 40" fill="var(--brown-dark)">
      <rect x="4" y="4" width="2" height="10"/><rect x="8" y="4" width="2" height="10"/><rect x="12" y="4" width="2" height="10"/>
      <path d="M4 13h10v3l-3 2v20H7V18l-3-2z"/>
      <circle cx="31" cy="21" r="14"/>
      <circle cx="31" cy="21" r="9" fill="var(--brown-light)"/>
      <circle cx="31" cy="21" r="6"/>
      <path d="M52 4c5 2 6 12 2 16v18h-4V4z"/>
    </svg>
  </div>
  <p class="meal-time" style="top:378px;">Dinner is served at 7:00 PM</p>

  <p class="note-line">• Open Bar from 6:00 p.m. - Midnight &nbsp; • Snacks available for purchase in front office.</p>

  <div class="band" style="left:0;top:479px;width:160px;height:9px;"></div>
  <h2 class="headline sub-title" style="left:171px;top:472px;">Room Amenities</h2>
  <div class="band" style="left:346px;top:479px;width:160px;height:9px;"></div>

  <div class="photo photo--giraffe" role="img" aria-label="Photo of a guest greeting a giraffe under ranch trees"></div>
  <svg class="chevron" style="top:574px;" height="52" viewBox="0 0 506 52" aria-hidden="true">
    <polygon points="0,0 506,0 506,4 253,46 0,4" fill="var(--paper)"/>
    <polyline points="0,6 253,48 506,6" fill="none" stroke="var(--ring-grey)" stroke-width="7" opacity="0.8"/>
  </svg>

  <div class="amenities">
    <div class="amenity">
      <svg width="44" height="28" viewBox="0 0 44 28" fill="var(--brown-dark)"><rect x="2" y="2" width="4" height="24"/><rect x="2" y="16" width="40" height="6"/><rect x="38" y="10" width="4" height="16"/><circle cx="12" cy="11" r="4"/><rect x="18" y="8" width="20" height="7" rx="2"/></svg>
      Plush<br>Bedding
    </div>
    <div class="amenity">
      <svg width="44" height="30" viewBox="0 0 44 30" fill="var(--brown-dark)"><rect x="10" y="0" width="6" height="5"/><rect x="7" y="5" width="12" height="24" rx="3"/><rect x="23" y="14" width="8" height="15" rx="2"/><ellipse cx="35" cy="22" rx="7" ry="6"/><circle cx="36" cy="12" r="2"/></svg>
      Shampoo<br>or Soap
    </div>
    <div class="amenity">
      <svg width="44" height="30" viewBox="0 0 44 30" fill="none" stroke="var(--brown-dark)" stroke-width="2.4"><path d="M10 12h20v6a10 10 0 0 1-20 0z"/><path d="M30 14h3a3 3 0 0 1 0 6h-3"/><path d="M6 28h30"/><path d="M17 9c-2-3 2-4 0-7M23 9c-2-3 2-4 0-7"/></svg>
      Coffee<br>Maker
    </div>
    <div class="amenity">
      <svg width="44" height="30" viewBox="0 0 44 30" fill="none" stroke="var(--brown-dark)" stroke-width="3.2" stroke-linecap="round"><path d="M6 12a22 22 0 0 1 32 0"/><path d="M12 18a13 13 0 0 1 20 0"/><path d="M18 23a5 5 0 0 1 8 0"/><circle cx="22" cy="27" r="1.5" fill="var(--brown-dark)"/></svg>
      In Room<br>Wifi
    </div>
    <div class="amenity">
      <svg width="44" height="30" viewBox="0 0 44 30" fill="var(--brown-dark)"><path d="M6 3h18v14H14z"/><circle cx="10" cy="10" r="7"/><rect x="12" y="16" width="6" height="13" rx="2"/><path d="M28 6h10M28 10h12M28 14h10" stroke="var(--brown-dark)" stroke-width="2" fill="none"/></svg>
      Hair<br>Dryer
    </div>
  </div>
</section>

<section class="page page--events">
  <div class="faint-name" style="top:300px;left:110px;">K.L. Creekside Lodge</div>

  <div class="band" style="left:0;top:68px;width:48px;height:18px;"></div>
  <p class="headline" style="left:100px;top:39px;font-size:18px;">events</p>
  <h1 class="headline page-title" style="left:64px;top:55px;">Special</h1>
  <div class="band" style="left:241px;top:68px;width:265px;height:18px;"></div>

  <div class="photo photo--deer" role="img" aria-label="Photo of a white-tailed deer in the brush"></div>

  <article class="event" style="top:117px;">
    <span class="event-tick"></span>
    <h3>Weddings</h3>
    <p>Lorem ipsum dolor sit amet, consectetuer adipiscing elit, sed diam nonummy nibh euismod tincidunt ut laoreet dolore magna aliquam erat volutpat.</p>
  </article>
  <article class="event" style="top:195px;">
    <span class="event-tick"></span>
    <h3>Corporate Retreats</h3>
    <p>Lorem ipsum dolor sit amet, consectetuer adipiscing elit, sed diam nonummy nibh euismod tincidunt ut laoreet dolore magna aliquam erat volutpat.</p>
  </article>
  <article class="event" style="top:274px;">
    <span class="event-tick"></span>
    <h3>Bus Tours</h3>
    <p>Lorem ipsum dolor sit amet, consectetuer adipiscing elit, sed diam nonummy nibh euismod tincidunt ut laoreet dolore magna aliquam erat volutpat.</p>
  </article>
  <article class="event" style="top:352px;">
    <span class="event-tick"></span>
    <h3>Family Reunion</h3>
    <p>Lorem ipsum dolor sit amet, consectetuer adipiscing elit, sed diam nonummy nibh euismod tincidunt ut laoreet dolore magna aliquam erat volutpat.</p>
  </article>
  <article class="event" style="top:431px;">
    <span class="event-tick"></span>
    <h3>Spring Break</h3>
    <p>Lorem ipsum dolor sit amet, consectetuer adipiscing elit, sed diam nonummy nibh euismod tincidunt ut laoreet dolore magna aliquam erat volutpat.</p>
  </article>

  <p class="quote">“many different venue options”</p>

  <div class="photo photo--wedding" role="img" aria-label="Photo of an outdoor ranch wedding ceremony beside a wooden cross and fence"></div>
  <svg class="chevron" style="top:574px;" height="50" viewBox="0 0 506 50" aria-hidden="true">
    <polygon points="0,0 506,0 506,4 253,44 0,4" fill="var(--paper)"/>
    <polyline points="0,6 253,46 506,6" fill="none" stroke="var(--ring-grey)" stroke-width="7" opacity="0.8"/>
  </svg>
</section>

</body>
</html>
```